Web-Redesign für Anbieter von immersiver Medienproduktion, Virtual Reality und 360-Grad-Aufnahmen
Zielgruppe
Bei dem Auftrag geht es um ein ReDesign der bestehende Website www.lumorix7.de
Lumorix 7 ist ein Powerhouse für immersive Medienproduktion, Virtual Reality und 360 Grad Aufnahmen. Wir erschaffen faszinierende und verblüffende Customer Experiences über alle Kanäle hinweg. Unsere Markeninszenierungen sind immer am Rande des technisch machbaren und hinterlassen nachhaltigen Eindruck beim Kunden. Dabei ist die Verbindung von hochwertigem Design, cutting-edge Technology und Emotion der Kern unserer Arbeit. Wir sind digital und real. Und Experten darin, Marken neuartig erfahrbar und damit erfolgreich zu machen. Nationale und internationale Kunden aus den Bereichen Automotive, Pharma, TV und Industrie vertrauen uns seit vielen Jahren.
Aufgabenstellung
Wir möchten unseren Slogan 'WE DO THE NEW' in den Fokus stellen und den Fokus auf uns Showreell samt 'Über uns'-Text legen. Wir wollen innovativ, futuristisch und aber klar strukturiert sein. Unser Ziel ist es, ein Termin mit dem potentiellen Interessenten zu haben.

```html
<!DOCTYPE html>
<html lang="de">
<head>
<meta charset="utf-8">
<title>Lumorix 7 – We do the new</title>
<link href="https://fonts.googleapis.com/css2?family=Poppins:wght@400;500;600;700;800&display=swap" rel="stylesheet">
<style>
:root{
  --navy:#0b2a5c;
  --navy-deep:#082150;
  --cyan:#3ee0e8;
  --blue-dot:#1f4fa8;
  --text:#0b2a5c;
  --white:#ffffff;
  --line:#9aa7bd;
}
*{box-sizing:border-box;margin:0;padding:0}
html,body{width:1200px;height:3634px;overflow:hidden;background:var(--white)}
body{font-family:'Poppins',sans-serif;color:var(--text);position:relative}
.abs{position:absolute}
.brand{font-family:'Poppins',sans-serif;font-weight:700;letter-spacing:.06em;white-space:nowrap}

.topbar{left:0;top:0;width:1200px;height:73px}
.topbar .address{left:87px;top:19px;font-size:15px}
.social{top:24px;display:flex;gap:14px;right:136px}
.social span{width:26px;height:24px;border:2.5px solid var(--navy);border-radius:5px;display:block}

.nav{left:0;top:73px;width:1200px;height:57px;background:var(--navy)}
.nav .brand{left:87px;top:15px;color:var(--white);font-size:20px}
.nav ul{position:absolute;right:135px;top:19px;list-style:none;display:flex;gap:34px}
.nav li{color:var(--white);font-size:14px;font-weight:500}
.nav li.active{color:var(--cyan)}

.hero{left:0;top:130px;width:1200px;height:545px;overflow:hidden}
.hero-bg{position:absolute;inset:0;background:
  radial-gradient(ellipse at 72% 30%,rgba(200,150,90,.55),transparent 55%),
  radial-gradient(ellipse at 60% 88%,rgba(170,30,50,.45),transparent 35%),
  linear-gradient(160deg,#1a120e 0%,#2f2118 45%,#14100f 100%)}
.hero h1{position:absolute;left:87px;top:72px;font-size:116px;line-height:124px;font-weight:800;color:var(--white);letter-spacing:-.01em}
.btn{position:absolute;height:56px;border-radius:28px;font-size:30px;letter-spacing:.08em;display:flex;align-items:center;justify-content:center}
.btn-solid{left:87px;top:367px;width:248px;background:var(--cyan);color:var(--navy)}
.btn-ghost{left:365px;top:367px;width:247px;border:2px solid var(--cyan);color:var(--cyan)}

.dots{display:flex;gap:6px}
.dots i{width:9px;height:9px;border-radius:50%;background:var(--navy);display:block}
.dots i:last-child{background:var(--cyan)}

.about-panel{left:0;top:675px;width:422px;height:537px;background:var(--navy)}
.about-panel .brand{left:0;width:422px;text-align:center;top:235px;color:var(--white);font-size:46px}
.about h2{position:absolute;right:90px;top:715px;font-size:60px;font-weight:700}
.about .dots{position:absolute;left:1063px;top:707px}
.about p{position:absolute;left:453px;width:660px;font-size:19px;line-height:31.2px}

.section-title{font-size:60px;font-weight:700;line-height:1}
.service .section-title{left:87px;top:1280px}
.service .dots{left:292px;top:1263px}
.card-img{position:absolute;top:1355px;width:323px;height:322px}
.card h3{position:absolute;font-size:34px;line-height:44px;font-weight:700;top:1693px}
.card p{position:absolute;font-size:16px;line-height:28.2px}

.clients{left:0;top:2237px;width:1200px;height:278px;background:var(--navy)}
.clients .section-title{left:87px;top:35px;color:var(--white)}
.client-row{position:absolute;left:75px;top:160px;width:1020px;display:flex;align-items:center;justify-content:space-between}
.client-row .name{color:var(--white);font-size:16px;font-weight:600;letter-spacing:.02em}
.client-row .name.big{font-size:26px}

.contact .section-title{left:87px;top:2588px}
.contact .dots{left:338px;top:2566px}
.field{position:absolute;left:87px;width:513px;border:1.5px solid var(--line);border-radius:30px;font-size:24px;color:#8a96aa;padding:14px 0 0 45px}
.btn-send{position:absolute;left:87px;top:3018px;width:219px;height:60px;border-radius:30px;background:var(--navy);color:var(--cyan);font-size:26px;font-weight:700;letter-spacing:.12em;display:flex;align-items:center;justify-content:center}
.contact-brand{left:730px;top:2745px;color:var(--navy);font-size:60px}

.footer .brand.logo{left:97px;top:3358px;color:var(--navy);font-size:32px}
.footer h4{position:absolute;top:3352px;font-size:20px;font-weight:600}
.footer .col{position:absolute;top:3393px;font-size:15px;line-height:26px}
.footer .col.small{font-size:13px;line-height:32px}
.footer .col.links{line-height:36px;font-size:15px}
.fsocial{position:absolute;left:448px;top:3487px;display:flex;gap:10px}
.fsocial span{width:30px;height:30px;border-radius:50%;background:var(--navy);display:block}
</style>
</head>
<body>

<header>
  <div class="abs topbar">
    <div class="abs address">Lichtfeldstraße 7, 82041 Oberhaching</div>
    <div class="abs social"><span></span><span></span><span></span></div>
  </div>
  <nav class="abs nav">
    <div class="abs brand">LUMORIX 7</div>
    <ul>
      <li class="active">HOME</li><li>ÜBER UNS</li><li>SERVICES</li><li>KONTAKT</li><li>TERMIN</li>
    </ul>
  </nav>
</header>

<section class="abs hero">
  <div class="hero-bg" role="img" aria-label="Showreel-Standbild: dunkle Eventhalle mit goldenen Lichtinstallationen und einem roten Fahrzeug"></div>
  <h1>WE DO<br>THE NEW</h1>
  <a class="btn btn-solid">SHOWREEL</a>
  <a class="btn btn-ghost">ÜBER UNS</a>
</section>

<section class="about">
  <div class="abs about-panel"><div class="abs brand">LUMORIX 7</div></div>
  <div class="dots"><i></i><i></i><i></i></div>
  <h2>ÜBER UNS</h2>
  <p style="top:808px">Lumorix 7 ist ein Powerhouse für immersive Medienproduktion, Virtual Reality und 360 Grad Aufnahmen. Wir erschaffen faszinierende und verblüffende Customer Experiences über alle Kanäle hinweg. Unsere Markeninszenierungen sind immer am Rande des technisch machbaren und hinterlassen nachhaltigen Eindruck beim Kunden. Dabei ist die Verbindung von hochwertigem Design, cutting-edge Technology und Emotion der Kern unserer Arbeit. Wir sind digital und real. Und Experten darin, Marken neuartig erfahrbar und damit erfolgreich zu machen. Nationale und internationale Kunden aus den Bereichen Automotive, Pharma, TV und Industrie vertrauen uns seit vielen Jahren.</p>
  <p style="top:1182px">Kommen Sie zu uns, wir können Zukunft.</p>
</section>

<section class="service">
  <div class="abs dots"><i></i><i></i><i></i></div>
  <h2 class="abs section-title">SERVICE</h2>

  <div class="card">
    <div class="card-img" style="left:87px;background:linear-gradient(180deg,#9fc4e0 0%,#6f8f6a 45%,#c0242f 80%,#8e1820 100%)" role="img" aria-label="Inszenierung auf rotem Teppich mit Palmen und Fotografen"></div>
    <h3 style="left:87px">DESIGN &amp; CONTENT<br>CREATION</h3>
    <p style="left:87px;top:1795px;width:335px">Wir entwickeln starke Marken und füllen sie mit Leben, um Ihre Marken und Produkte unwiderstehlich zu machen. Wir glauben an klares, einprägsames und hochwertiges Design, das die Kraft emotionaler Geschichten nutzt. Dabei beobachten wir das Markenumfeld und suchen immer nach neuen Wegen, um Ihre Zielgruppe zu erreichen – über Kopf UND Herz. Unsere Expertise umfasst Design für TV-Sender und TV-Formate, TV-Kampagnen, Messebespielungen, Imagefilme, Werbespots und Social Media Filme.</p>
  </div>

  <div class="card">
    <div class="card-img" style="left:443px;background:linear-gradient(180deg,#1d4a44 0%,#3f7f72 45%,#1a3a38 100%)" role="img" aria-label="Virtueller Showroom mit grünlichem Licht und spiegelndem Boden"></div>
    <h3 style="left:443px">REALTIME<br>EXPERIENCES</h3>
    <p style="left:441px;top:1795px;width:330px">Sie planen eine Veranstaltung, Messe oder ein besonders Corporate Event auszurichten? Ein Event, welches eine beeindruckende, immersive Erfahrung bietet? Dann lassen Sie uns sprechen. Seit über 20 Jahren arbeiten wir in der professionellen Event-Planung im Bereich Immersive Events. Wir kreieren Ereignisse, die den Zuschauer faszinieren und ihn mittels neuester Technologien in eine andere Welt abtauchen lassen.</p>
  </div>

  <div class="card">
    <div class="card-img" style="left:790px;background:linear-gradient(120deg,#c8342c 0%,#7a3d2a 45%,#e0a43a 80%,#c98a2e 100%)" role="img" aria-label="Gruppe junger Zuschauer in warmem Licht"></div>
    <h3 style="left:787px">VIDEO<br>PERFORMANCE<br>MARKETING</h3>
    <p style="left:787px;top:1839px;width:330px">Sie planen eine Veranstaltung, Messe oder ein besonders Corporate Event auszurichten? Ein Event, welches eine beeindruckende, immersive Erfahrung bietet? Dann lassen Sie uns sprechen. Seit über 20 Jahren arbeiten wir in der professionellen Event-Planung im Bereich Immersive Events. Wir kreieren Ereignisse, die den Zuschauer faszinieren und ihn mittels neuester Technologien in eine andere Welt abtauchen lassen.</p>
  </div>
</section>

<section class="abs clients">
  <h2 class="abs section-title">KUNDEN</h2>
  <div class="client-row">
    <svg width="16" height="24" viewBox="0 0 16 24"><path d="M12 3 L4 12 L12 21" fill="none" stroke="#fff" stroke-width="3"/></svg>
    <span class="name big">Nordwelle</span>
    <span class="name">Lernkompass</span>
    <span class="name">Tellerbote</span>
    <span class="name">Angebotsfuchs</span>
    <span class="name">Glasklar</span>
    <span class="name">Kanalfeld Media</span>
    <svg width="16" height="24" viewBox="0 0 16 24"><path d="M4 3 L12 12 L4 21" fill="none" stroke="#fff" stroke-width="3"/></svg>
  </div>
</section>

<section class="contact">
  <div class="abs dots"><i></i><i></i><i></i></div>
  <h2 class="abs section-title">KONTAKT</h2>
  <div class="field" style="top:2675px;height:59px">Name</div>
  <div class="field" style="top:2752px;height:59px">Email</div>
  <div class="field" style="top:2829px;height:163px">Nachricht</div>
  <a class="btn-send">SENDEN</a>
  <div class="abs brand contact-brand">LUMORIX 7</div>
</section>

<footer class="footer">
  <div class="abs brand logo">LUMORIX 7</div>
  <h4 style="left:448px">KONTAKT</h4>
  <div class="col" style="left:448px">Lumorix 7<br>Lichtfeldstraße 7<br>82041 Oberhaching</div>
  <div class="fsocial"><span></span><span></span><span></span></div>
  <h4 style="left:685px">PARTNER LINKS</h4>
  <div class="col small" style="left:685px;top:3386px">Jonas Ferber Kreativstudio<br>Blattwerk Post<br>Achtzig Medien Service</div>
  <h4 style="left:942px">QUICK LINKS</h4>
  <div class="col links" style="left:942px;top:3386px">Über uns<br>Services<br>Kontakt<br>Cookie-Richtlinie (EU)<br>Haftungsausschluss<br>Impressum</div>
</footer>

</body>
</html>
```